Awesome WYSIWYG

I'm looking for someone to redesign this WYSIWYG Editor that I've developed. I'm looking for a really cool and modern design that will leave my clients stunned. Hopefully, this tool will be embedded into a software package which is currently used around the world.
I need to add a character count to the design and I would like my logo incorporated somewhere into the design as well. Otherwise, I'm not fussed about the layout, feel free to move elements around.
I'm expecting that the designer will provide all icons, color codes and anything else I will need to recreate the design exactly within my development environment.
This is an example of the type of wow I'm looking for:
https://pixelvane.example/shots/4827163-Free-Flat-Wysiwyg-Text-Editor-Kit
I'm happy to receive the icon files in vector format or high quality jpg. Ideally vectors would be best. At a guess, I expect the icons will need to be scaled to as big as 30px square.
Icons Needed: Set BG Color, set font color, create hyperlink, remove hyperlink, QuillPath IT logo (links to my website), cut, copy, paste, bold, underline, italic, text align left, text align center, text justify, text align right, indent line, outdent line, bulleted list, numbered list, save button (currently just has text "update changes")

```html
<!DOCTYPE html>
<html lang="en">
<head>
<meta charset="utf-8">
<title>Awesome WYSIWYG – Toolbar Redesign</title>
<link rel="stylesheet" href="https://fonts.googleapis.com/css2?family=Open+Sans:wght@400;600;700&family=Roboto:ital,wght@0,400;0,500;0,700;1,700&family=Tinos:wght@400;700&display=swap">
<style>
:root{
  --blue:#0e8fd6;
  --blue-dark:#065f93;
  --blue-active:#05669c;
  --divider:#7cc6ee;
  --band:#5b5b5b;
  --ink:#2f2f2f;
  --frame:#555555;
  --orange:#f2652b;
  --link-grey:#676767;
  --faint:#d0d0d0;
  --label-blue:#1c8fd2;
  --old-ink:#24427a;
  --paper:#ffffff;
  --fade:#ececec;
}
*{box-sizing:border-box;margin:0;padding:0}
html,body{width:1200px;height:2556px;overflow:hidden;background:var(--paper)}
.canvas{position:relative;width:1200px;height:2556px;overflow:hidden;font-family:"Roboto",Arial,sans-serif;
  background:linear-gradient(180deg,var(--paper) 0,var(--paper) 1840px,var(--fade) 2100px,var(--fade) 100%)}
.abs{position:absolute}
.section-label{font-size:15px;font-weight:700;color:var(--ink)}
.section-label.blue{color:var(--label-blue)}
.side-note{position:absolute;transform:translate(-50%,-50%) rotate(-90deg);white-space:nowrap;font-size:17px;color:#3a3a3a}

/* legacy band */
.legacy-band{left:0;top:222px;width:1200px;height:206px;background:var(--band)}
.legacy-bar{left:44px;top:266px;width:836px;height:116px;background:linear-gradient(#fbfbfb,#e6e9ee);border:2px solid #b9bfc8;border-radius:4px;color:var(--old-ink)}
.legacy-row{position:absolute;left:10px;right:10px;height:50px;display:flex;align-items:center;gap:14px}
.legacy-row.r1{top:6px}.legacy-row.r2{top:60px}
.legacy-bar .sep{width:2px;height:34px;background:#c3c8d0}
.legacy-bar svg{width:30px;height:30px}
.legacy-bar .old-b{font-family:"Tinos",serif;font-weight:700;font-size:32px;color:#234c9a}
.legacy-bar .old-i{font-style:italic}
.legacy-bar .old-u{text-decoration:underline}
.legacy-select{font-family:"Open Sans",sans-serif;font-size:26px;color:#222;display:flex;align-items:center;gap:14px}
.legacy-select svg{width:14px;height:10px}
.legacy-mark{width:30px;height:30px;border:3px solid #1d6bc0;border-radius:50%}

/* toolbars */
.toolbar{display:flex;background:var(--blue);color:#fff}
.cell{display:flex;align-items:center;justify-content:center;flex:none;position:relative}
.cell.active{background:var(--blue-active)}
.cell.split{border-left:2px solid var(--divider)}
.glyph-b{font-weight:700}
.glyph-i{font-weight:700;font-style:italic}
.glyph-u{font-weight:500;text-decoration:underline;text-underline-offset:.18em;text-decoration-thickness:.09em}

.main-bar{left:46px;top:476px;width:1108px;height:72px;border-radius:4px}
.main-bar .cell{width:74.6px;height:72px;font-size:28px}
.main-bar svg{width:30px;height:30px}

.tile-row{left:46px;width:1108px;height:220px;border-radius:18px;overflow:hidden}
.tile-row .cell{width:221.6px;height:220px;font-size:78px}
.tile-row svg{width:84px;height:84px}
.tile-row.t1{top:836px}.tile-row.t2{top:1074px}.tile-row.t3{top:1310px}

/* controls */
.select{display:flex;align-items:center;justify-content:space-between;border:2px solid var(--frame);border-radius:4px;background:#fff;font-family:"Open Sans",sans-serif;color:var(--ink)}
.select .caret{width:16px;height:10px;color:#333}
.swatch-box,.style-box{border:2px solid var(--frame);border-radius:4px;background:#fff;display:flex;align-items:center;justify-content:center;color:#444}
.swatch{background:var(--orange);border-radius:4px}
.link-box{background:var(--link-grey);border-radius:4px;display:flex;align-items:center;justify-content:center;color:#fff}

.font-select{left:46px;top:560px;width:330px;height:54px;padding:0 16px 0 18px;font-family:"Tinos",serif;font-size:27px}
.size-select{left:388px;top:560px;width:164px;height:54px;padding:0 14px 0 18px;font-size:26px}
.color-pick{left:564px;top:560px;width:56px;height:54px}
.color-pick .swatch{width:38px;height:36px}
.font-color{left:630px;top:560px;width:54px;height:54px}
.font-color svg{width:36px;height:36px}
.link-pick{left:694px;top:560px;width:58px;height:54px}
.link-pick svg{width:32px;height:32px}

.credit{font-family:"Roboto",sans-serif;color:#9a9a9a;text-align:right;line-height:1}
.credit .by{display:block;font-size:15px;font-weight:500}
.credit .name{display:block;font-size:17px;font-weight:700}
.credit-wrap{display:flex;align-items:center;gap:6px}
.credit-dot{border:3px solid #9a9a9a;border-radius:50%}
.credit-main{right:46px;top:572px}
.credit-main .credit-dot{width:34px;height:34px}

/* faint preview text */
.preview{left:46px;top:620px;width:1108px;height:240px;border:2px solid #f1f1f1;border-top:none;font-family:"Tinos",serif;color:var(--faint);padding:26px 24px}
.preview h3{font-size:32px;font-weight:700;text-decoration:underline;line-height:1.2}
.preview p{font-size:30px;line-height:40px;margin-top:6px;width:1000px}
.preview h4{font-size:30px;font-weight:700;text-decoration:underline;margin-top:28px}

/* large controls */
.big-size{left:46px;top:1548px;width:514px;height:168px;border:5px solid var(--frame);border-radius:18px;padding:0 52px 0 74px;font-size:72px;font-weight:600;letter-spacing:2px}
.big-size .caret{width:44px;height:26px}
.big-color{left:588px;top:1548px;width:170px;height:168px;border:5px solid var(--frame);border-radius:18px}
.big-color .swatch{width:110px;height:106px;border-radius:16px}
.big-font{left:784px;top:1548px;width:172px;height:168px;border:5px solid var(--frame);border-radius:18px}
.big-font svg{width:112px;height:112px}
.big-link{left:982px;top:1548px;width:172px;height:168px;border-radius:18px}
.big-link svg{width:100px;height:100px}

/* sliced assets */
.size-label{font-family:"Open Sans",sans-serif;font-size:25px;color:#555;left:70px}
.size-label small{font-size:22px;color:#888}
.rule{left:160px;top:2050px;width:2px;height:180px;background:#333}
.slice-row{left:210px;display:flex;gap:12px}
.slice{width:52px;height:52px;border-radius:5px;display:flex;align-items:center;justify-content:center;color:#fff;font-size:22px}
.slice svg{width:26px;height:26px}
.slice-row.light .slice{background:var(--blue)}
.slice-row.dark .slice{background:var(--blue-dark)}
.slice-row.light{top:2054px}.slice-row.dark{top:2118px}
.sliver{width:16px;height:52px;background:var(--blue);border-radius:3px}
.sliver.end{width:14px;border-radius:0 5px 5px 0}
.mini-row{left:210px;top:2186px;height:42px;display:flex;align-items:center;gap:10px}
.mini{height:42px;border-radius:5px;display:flex;align-items:center;justify-content:center}
.mini.white{background:#fff;width:42px;border:1px solid #ccc}
.mini.split-l{width:46px;border-radius:5px 0 0 5px;background:#fff;border:1px solid #ccc}
.mini.split-r{width:44px;border-radius:0 5px 5px 0;background:#fff;border:1px solid #ccc;margin-left:-10px}
.mini.split-r svg{width:12px;height:8px;color:#333}
.mini.black{background:#000;width:42px}
.mini.black-frame{background:#000;width:42px;padding:6px}
.mini.black-frame span{display:block;width:100%;height:100%;background:#fff;border-radius:4px}
.mini.font-a{background:#000;width:42px;color:#fff}
.mini.font-a svg{width:28px;height:28px}
.mini.link-w{background:#fff;width:42px;border:1px solid #ccc;color:#444}
.mini.link-g{background:var(--link-grey);width:42px;color:#fff}
.mini svg{width:24px;height:24px}
.credit-mini .by{font-size:11px}.credit-mini .name{font-size:12px}
.credit-mini .credit-dot{width:24px;height:24px;border-width:2px}
</style>
</head>
<body>
<svg width="0" height="0" style="position:absolute" aria-hidden="true">
  <defs>
    <symbol id="i-align-left" viewBox="0 0 24 24"><path d="M4 6h16M4 10h10M4 14h16M4 18h10" stroke="currentColor" stroke-width="2.4" stroke-linecap="round" fill="none"/></symbol>
    <symbol id="i-align-center" viewBox="0 0 24 24"><path d="M4 6h16M7 10h10M4 14h16M7 18h10" stroke="currentColor" stroke-width="2.4" stroke-linecap="round" fill="none"/></symbol>
    <symbol id="i-align-right" viewBox="0 0 24 24"><path d="M4 6h16M10 10h10M4 14h16M10 18h10" stroke="currentColor" stroke-width="2.4" stroke-linecap="round" fill="none"/></symbol>
    <symbol id="i-justify" viewBox="0 0 24 24"><path d="M4 6h16M4 10h16M4 14h16M4 18h16" stroke="currentColor" stroke-width="2.4" stroke-linecap="round" fill="none"/></symbol>
    <symbol id="i-indent" viewBox="0 0 24 24"><path d="M2.5 8.5l3.5 3.5-3.5 3.5M9 5v14M12.5 6h9M12.5 10h9M12.5 14h9M12.5 18h9" stroke="currentColor" stroke-width="2.4" stroke-linecap="round" stroke-linejoin="round" fill="none"/></symbol>
    <symbol id="i-outdent" viewBox="0 0 24 24"><path d="M21.5 8.5L18 12l3.5 3.5M15 5v14M2.5 6h9M2.5 10h9M2.5 14h9M2.5 18h9" stroke="currentColor" stroke-width="2.4" stroke-linecap="round" stroke-linejoin="round" fill="none"/></symbol>
    <symbol id="i-bullets" viewBox="0 0 24 24"><circle cx="4.5" cy="6" r="2" fill="currentColor"/><circle cx="4.5" cy="12" r="2" fill="currentColor"/><circle cx="4.5" cy="18" r="2" fill="currentColor"/><path d="M10 6h11M10 12h11M10 18h11" stroke="currentColor" stroke-width="2.4" stroke-linecap="round"/></symbol>
    <symbol id="i-numbered" viewBox="0 0 24 24"><g fill="currentColor" font-family="Roboto,sans-serif" font-weight="700" font-size="6.5"><text x="2" y="8">1</text><text x="2" y="14.2">2</text><text x="2" y="20.4">3</text></g><path d="M10 6h11M10 12h11M10 18h11" stroke="currentColor" stroke-width="2.4" stroke-linecap="round"/></symbol>
    <symbol id="i-cut" viewBox="0 0 24 24"><g stroke="currentColor" stroke-width="2.4" stroke-linecap="round" fill="none"><circle cx="6.5" cy="17" r="3.3"/><circle cx="17.5" cy="17" r="3.3"/><path d="M8.6 14.4L16 3M15.4 14.4L8 3"/></g></symbol>
    <symbol id="i-copy" viewBox="0 0 24 24"><g stroke="currentColor" stroke-width="2.4" fill="none"><path d="M13.5 8.5V6a3 3 0 0 0-3-3H6a3 3 0 0 0-3 3v4.5a3 3 0 0 0 3 3h2.5"/><rect x="8.5" y="8.5" width="12.5" height="12.5" rx="3"/></g></symbol>
    <symbol id="i-paste" viewBox="0 0 24 24"><rect x="3" y="3" width="16" height="16" rx="3.5" stroke="currentColor" stroke-width="2.4" fill="none"/><rect x="7.5" y="10" width="14" height="11" rx="3" fill="currentColor"/></symbol>
    <symbol id="i-link" viewBox="0 0 24 24"><g transform="rotate(-45 12 12)" stroke="currentColor" stroke-width="2.4" fill="none" stroke-linecap="round"><rect x="1.5" y="8.5" width="10.5" height="7" rx="3.5"/><rect x="12" y="8.5" width="10.5" height="7" rx="3.5"/><path d="M8.5 12h7"/></g></symbol>
    <symbol id="i-font-color" viewBox="0 0 24 24"><path d="M6.5 16.5L12 3.5l5.5 13M8.6 12h6.8" stroke="currentColor" stroke-width="2.4" stroke-linejoin="round" fill="none"/><rect x="4" y="19" width="16" height="2.8" rx="1.4" fill="currentColor"/></symbol>
    <symbol id="i-caret" viewBox="0 0 16 10"><path d="M0 0h16L8 10z" fill="currentColor"/></symbol>
    <symbol id="i-highlight" viewBox="0 0 24 24"><text x="3" y="11" font-family="Tinos,serif" font-size="10" fill="#b8860b">ab</text><path d="M4 20l12-8 3 3-8 6z" fill="currentColor"/><rect x="2" y="21" width="20" height="2" fill="#e6c600"/></symbol>
  </defs>
</svg>

<main class="canvas">
  <p class="abs section-label" style="left:48px;top:190px">Original Toolbar Assets</p>

  <section class="abs legacy-band" aria-label="Legacy toolbar">
  </section>
  <div class="abs legacy-bar">
    <div class="legacy-row r1">
      <svg><use href="#i-highlight"/></svg>
      <svg><use href="#i-font-color"/></svg>
      <span class="sep"></span>
      <svg><use href="#i-link"/></svg>
      <svg style="opacity:.5"><use href="#i-link"/></svg>
      <span class="sep"></span>
      <span class="legacy-select">Font Size <svg><use href="#i-caret"/></svg></span>
      <span class="legacy-select">Font Family <svg><use href="#i-caret"/></svg></span>
      <span class="sep"></span>
      <span class="legacy-mark"></span>
    </div>
    <div class="legacy-row r2">
      <svg><use href="#i-cut"/></svg>
      <svg><use href="#i-copy"/></svg>
      <svg><use href="#i-paste"/></svg>
      <span class="sep"></span>
      <span class="old-b">B</span>
      <span class="old-b old-u">U</span>
      <span class="old-b old-i">I</span>
      <span class="sep"></span>
      <svg><use href="#i-align-left"/></svg>
      <svg><use href="#i-align-center"/></svg>
      <svg><use href="#i-justify"/></svg>
      <svg><use href="#i-align-right"/></svg>
      <span class="sep"></span>
      <svg><use href="#i-indent"/></svg>
      <svg><use href="#i-outdent"/></svg>
      <span class="sep"></span>
      <svg><use href="#i-bullets"/></svg>
      <svg><use href="#i-numbered"/></svg>
    </div>
  </div>

  <p class="abs section-label blue" style="left:46px;top:442px">Redesigned Toolbar</p>

  <nav class="abs toolbar main-bar" aria-label="Editor toolbar">
    <span class="cell glyph-b">B</span>
    <span class="cell glyph-i">i</span>
    <span class="cell glyph-u">U</span>
    <span class="cell active"><svg><use href="#i-align-left"/></svg></span>
    <span class="cell"><svg><use href="#i-align-center"/></svg></span>
    <span class="cell"><svg><use href="#i-align-right"/></svg></span>
    <span class="cell"><svg><use href="#i-justify"/></svg></span>
    <span class="cell split"><svg><use href="#i-indent"/></svg></span>
    <span class="cell"><svg><use href="#i-outdent"/></svg></span>
    <span class="cell"><svg><use href="#i-bullets"/></svg></span>
    <span class="cell"><svg><use href="#i-numbered"/></svg></span>
    <span class="cell split"><svg><use href="#i-cut"/></svg></span>
    <span class="cell"><svg><use href="#i-copy"/></svg></span>
    <span class="cell"><svg><use href="#i-paste"/></svg></span>
  </nav>

  <div class="abs preview">
    <h3>Tye best item</h3>
    <p>This is a description of the item, it is a very good item which I think will sell very well.</p>
    <h4>Evaluation</h4>
  </div>

  <div class="abs select font-select"><span>Times New Roman</span><svg class="caret"><use href="#i-caret"/></svg></div>
  <div class="abs select size-select"><span>16 pt</span><svg class="caret"><use href="#i-caret"/></svg></div>
  <div class="abs swatch-box color-pick"><span class="swatch"></span></div>
  <div class="abs style-box font-color"><svg><use href="#i-font-color"/></svg></div>
  <div class="abs link-box link-pick"><svg><use href="#i-link"/></svg></div>
  <div class="abs credit-wrap credit-main">
    <div class="credit"><span class="by">brought by</span><span class="name">QuillPath IT</span></div>
    <span class="credit-dot"></span>
  </div>

  <span class="side-note" style="left:22px;top:1284px">Custom Toolbar Icon Designs, High-Resolution Vector Assets</span>

  <div class="abs toolbar tile-row t1">
    <span class="cell glyph-b">B</span>
    <span class="cell glyph-i">i</span>
    <span class="cell glyph-u">U</span>
    <span class="cell active split"><svg><use href="#i-align-left"/></svg></span>
    <span class="cell"><svg><use href="#i-align-center"/></svg></span>
  </div>
  <div class="abs toolbar tile-row t2">
    <span class="cell"><svg><use href="#i-align-right"/></svg></span>
    <span class="cell"><svg><use href="#i-justify"/></svg></span>
    <span class="cell split"><svg><use href="#i-indent"/></svg></span>
    <span class="cell"><svg><use href="#i-outdent"/></svg></span>
    <span class="cell"><svg><use href="#i-bullets"/></svg></span>
  </div>
  <div class="abs toolbar tile-row t3">
    <span class="cell"><svg><use href="#i-numbered"/></svg></span>
    <span class="cell split"><svg><use href="#i-cut"/></svg></span>
    <span class="cell"><svg><use href="#i-copy"/></svg></span>
    <span class="cell"><svg><use href="#i-paste"/></svg></span>
  </div>

  <div class="abs select big-size"><span>16 pt</span><svg class="caret"><use href="#i-caret"/></svg></div>
  <div class="abs swatch-box big-color"><span class="swatch"></span></div>
  <div class="abs style-box big-font"><svg><use href="#i-font-color"/></svg></div>
  <div class="abs link-box big-link"><svg><use href="#i-link"/></svg></div>

  <span class="side-note" style="left:22px;top:2130px">100% Sliced Transparent Assets (Icons, Masks)</span>

  <p class="abs size-label" style="top:2062px">36 <small>px</small></p>
  <p class="abs size-label" style="top:2126px">36 <small>px</small></p>
  <p class="abs size-label" style="top:2188px">28 <small>px</small></p>
  <span class="abs rule"></span>

  <div class="abs slice-row light">
    <span class="slice glyph-b">B</span>
    <span class="slice glyph-i">i</span>
    <span class="slice glyph-u">U</span>
    <span class="slice"><svg><use href="#i-align-left"/></svg></span>
    <span class="slice"><svg><use href="#i-align-center"/></svg></span>
    <span class="slice"><svg><use href="#i-align-right"/></svg></span>
    <span class="slice"><svg><use href="#i-justify"/></svg></span>
    <span class="slice"><svg><use href="#i-indent"/></svg></span>
    <span class="slice"><svg><use href="#i-outdent"/></svg></span>
    <span class="slice"><svg><use href="#i-bullets"/></svg></span>
    <span class="slice"><svg><use href="#i-numbered"/></svg></span>
    <span class="slice"><svg><use href="#i-cut"/></svg></span>
    <span class="slice"><svg><use href="#i-copy"/></svg></span>
    <span class="slice"><svg><use href="#i-paste"/></svg></span>
    <span class="sliver"></span>
    <span class="sliver end" style="margin-left:-4px"></span>
  </div>
  <div class="abs slice-row dark">
    <span class="slice glyph-b">B</span>
    <span class="slice glyph-i">i</span>
    <span class="slice glyph-u">U</span>
    <span class="slice"><svg><use href="#i-align-left"/></svg></span>
    <span class="slice"><svg><use href="#i-align-center"/></svg></span>
    <span class="slice"><svg><use href="#i-align-right"/></svg></span>
    <span class="slice"><svg><use href="#i-justify"/></svg></span>
    <span class="slice"><svg><use href="#i-indent"/></svg></span>
    <span class="slice"><svg><use href="#i-outdent"/></svg></span>
    <span class="slice"><svg><use href="#i-bullets"/></svg></span>
    <span class="slice"><svg><use href="#i-numbered"/></svg></span>
    <span class="slice"><svg><use href="#i-cut"/></svg></span>
    <span class="slice"><svg><use href="#i-copy"/></svg></span>
    <span class="slice"><svg><use href="#i-paste"/></svg></span>
  </div>
  <div class="abs mini-row">
    <span class="mini split-l"></span>
    <span class="mini split-r"><svg><use href="#i-caret"/></svg></span>
    <span class="mini white"></span>
    <span class="mini black-frame"><span></span></span>
    <span class="mini font-a"><svg><use href="#i-font-color"/></svg></span>
    <span class="mini link-w"><svg><use href="#i-link"/></svg></span>
    <span class="mini link-g"><svg><use href="#i-link"/></svg></span>
    <span class="credit-wrap credit-mini" style="margin-left:8px">
      <span class="credit"><span class="by">brought by</span><span class="name">QuillPath IT</span></span>
      <span class="credit-dot"></span>
    </span>
  </div>
</main>
</body>
</html>
```